WP website design (Thistlewaite)

We need a wordpress design for an established auction and real estate company based in Viginia- "The Name That Closes!". The winning design will incorporate a professional color scheme with company logo in a clean layout. The design needs to consider that this will be developed on a responsive theme.
Industry/Entity Type
Real Estate
Requirements
Must have
- - - We will require winning designer to provide a layered PSD (Adobe photoshop) concept file, along with any non-standard font files used.
- Logo attached. Color scheme should compliment the logo colors; nothing flashy, rather more business oriented … subdued colors. Lighten up the burgundy color; not so dark on the background;
- Horizontal Navigation menu with these pages:
- Home - Upcoming Auctions - Appraisals - Past Auctions - Real Estate for Sale Sellers - Buyers - About Thistlewaite - Contact Us
- A slideshow element on the home page use stock of real estate for the initial image.
- Sidebar widgets to be included are: Email sign-up form - Featured Auctions - Testimonial widget - 'Our Videos' widget; Social media icons somewhere in layout (facebook, twitter, RSS, and Youtube, linkedIn), News & Events widget, "Special announcements" blog.
- Homepage content is text:
- Thistlewaite is "The name that closes!"
- Thistlewaite Auctioneers International is a premier, full service Auction Company specializing in the sale of commercial and residential real estate through the auction method. In the last 53 years, we have conducted thousands of auctions across the United States and several foreign countries.
- We bring our years of experience in auctioning homes, land, condominiums, industrial properties, retail buildings and development sites to help private individuals, corporations and financial institutions sell their property. In addition, we can assist you with liquidating estates, antiques, equipment and firearms collections.
- We have conducted thousands of auctions, assisting a wide range of companies both large and small achieve maximum value for their capital assets.
Nice to have
- Site will have drop down menus, please show what one will look like.
Should not have
- no gavels should be used in the design

```html
<!DOCTYPE html>
<html lang="en">
<head>
<meta charset="utf-8">
<title>Thistlewaite Auctioneers International</title>
<link href="https://fonts.googleapis.com/css2?family=Dosis:wght@500;600;700&family=Didact+Gothic&family=Open+Sans:wght@400;600;700&family=Oswald:wght@500&display=swap" rel="stylesheet">
<style>
:root{
  --red:#c62f2d;
  --ink:#1d1d1d;
  --text:#2a2a2a;
  --page:#e9e9e9;
  --panel:#2b2b2b;
  --link:#4a5bc4;
  --olive:#6e5c1f;
  --gold:#f2d23a;
}
*{box-sizing:border-box;margin:0;padding:0}
html,body{width:686px;height:1200px;overflow:hidden}
body{position:relative;background:var(--page);font-family:"Open Sans",Arial,sans-serif;color:var(--text)}

/* header */
.site-header{position:absolute;left:0;top:0;width:686px;height:113px;background:linear-gradient(#ececec,#e2e2e2)}
.brand{position:absolute;left:12px;top:12px;font-family:"Dosis",sans-serif;font-weight:700;color:var(--red)}
.brand-name{font-size:26px;line-height:24px;letter-spacing:.3px}
.brand-sub{font-size:11px;line-height:14px;margin-top:2px;padding-left:2px}
.brand-tag{position:absolute;left:70px;top:76px;font-size:7px;color:#333}
.alliance{position:absolute;left:14px;top:89px;font-size:9px;color:#222}
.social{position:absolute;top:10px;right:10px;display:flex;gap:9px}
.social span{width:24px;height:24px;border-radius:50%;background:#8f97a4;border:1px solid #7a8190}
.phone-band{position:absolute;left:478px;top:68px;width:208px;height:28px}
.phone-band .txt{position:absolute;left:46px;top:1px;font-family:"Oswald",sans-serif;font-size:18px;color:#fff;letter-spacing:.5px}

/* nav */
.main-nav{position:absolute;left:0;top:113px;width:686px;height:26px;background:var(--red);display:flex;font-size:9.5px;color:#fff;text-transform:uppercase}
.main-nav a{display:flex;align-items:center;justify-content:center;border-right:1px solid #dc6b68;height:100%;color:#fff;text-decoration:none}
.dropdown{position:absolute;left:54px;top:139px;width:124px;height:65px;background:rgba(90,80,30,.78);padding:4px 0 0 10px;font-size:8.5px;color:#fff;line-height:19px}

/* slider */
.hero{position:absolute;left:0;top:139px;width:686px;height:286px;background:linear-gradient(180deg,#c5d3c9 0%,#5f7f4a 30%,#e8ebe6 55%,#3aa9d2 75%,#d7d7d2 100%)}
.hero-arrow{position:absolute;top:270px;width:20px;height:20px;border-radius:50%;background:rgba(120,120,120,.8)}
.hero-dots{position:absolute;left:312px;top:403px;display:flex;gap:4px}
.hero-dots span{width:12px;height:12px;border:1px solid #fff;background:rgba(255,255,255,.6)}
.hero-dots span.on{background:#9b2b2a}

/* welcome */
.welcome-title{position:absolute;left:12px;top:455px;font-family:"Didact Gothic",sans-serif;font-weight:400;font-size:16.5px;color:var(--red);white-space:nowrap}
.welcome-text{position:absolute;left:12px;top:478px;width:462px;font-family:"Didact Gothic",sans-serif;font-size:10.4px;line-height:14px;color:#222;letter-spacing:.1px}

/* newsletter */
.newsletter{position:absolute;left:484px;top:460px;width:189px;height:115px;background:linear-gradient(#cf3a36,#b8292a);border-radius:4px}
.newsletter .ico{position:absolute;left:36px;top:12px;width:30px;height:30px;background:#f4f4f4;border-radius:2px}
.newsletter h3{position:absolute;left:86px;top:8px;font-family:"Dosis",sans-serif;font-weight:500;font-size:15px;line-height:19px;color:#fff}
.newsletter .field{position:absolute;left:23px;top:55px;width:141px;height:21px;border:1px solid #e7a9a7;background:#b42624;color:#fff;font-size:8px;padding:5px 4px}
.newsletter .btn{position:absolute;left:59px;top:85px;width:69px;height:19px;background:#c7ab58;border:1px solid #f2e4b0;border-radius:3px;color:#2b2b2b;font-size:9px;font-weight:700;text-align:center;line-height:17px}

/* auctions */
.section-title{position:absolute;font-family:"Open Sans",sans-serif;font-weight:400;font-size:15px;color:#222}
.pager{position:absolute;left:433px;top:552px;display:flex;gap:2px}
.pager span{width:17px;height:18px;background:var(--red);display:flex;align-items:center;justify-content:center}
.auction-card{position:absolute;top:576px;width:223px;height:292px;background:#fafafa;border:1px solid #bbb;font-family:Arial,"Open Sans",sans-serif}
.auction-card .head{height:21px;background:#0e0e0e;color:#fff;font-size:10px;padding:4px 12px}
.auction-card .photo{position:absolute;left:3px;top:35px;width:217px;height:69px;background:linear-gradient(#8fb6e6 0%,#b9cde6 40%,#9d7a68 60%,#5d8a3e 100%)}
.auction-card .links{position:absolute;left:12px;top:142px;width:200px;font-size:10px;color:var(--link);display:flex;justify-content:space-between}
.auction-card .links i{display:inline-block;width:12px;height:11px;background:#e1b824;margin-right:4px;vertical-align:-1px}
.auction-card .links i.d{background:#5a8fd0}
.auction-card .kind{position:absolute;left:12px;top:163px;font-size:11px;color:var(--olive)}
.auction-card .meta{position:absolute;left:12px;font-size:10.5px;color:#222;white-space:nowrap}
.auction-card .meta b{color:var(--olive)}
.auction-card .bid{position:absolute;left:12px;top:216px;font-size:10px;color:var(--link);display:flex;align-items:center}
.auction-card .bid i{width:22px;height:13px;background:#9aa6b6;margin-right:6px}
.auction-card p{position:absolute;left:12px;top:234px;width:202px;font-size:9.5px;line-height:12.4px;color:#222}

/* sidebar dark widgets */
.dark-widget{position:absolute;left:484px;width:189px;background:var(--panel);border:1px solid #1b1b1b;border-radius:3px}
.dark-widget .bar{margin:2px;height:23px;background:var(--red);color:#fff;font-family:"Dosis",sans-serif;font-weight:600;font-size:13.5px;text-align:center;line-height:23px}
.upcoming .sub{text-align:center;font-size:9.5px;color:#eee;margin-top:8px}
.upcoming .photo{position:absolute;left:14px;top:55px;width:159px;height:77px;border:2px solid #b12b2a;background:linear-gradient(#a8c0dc,#d8d4cc 55%,#5a8a3a)}
.upcoming .date{position:absolute;left:0;width:100%;top:141px;text-align:center;font-size:10px;color:#fff}
.upcoming .btn{position:absolute;left:59px;top:162px;width:68px;height:20px;background:#3c3f44;border:1px solid #565a60;border-radius:2px;color:#fff;font-size:9px;text-align:center;line-height:18px}
.news ul{list-style:none;padding:14px 12px 0 18px}
.news li{position:relative;font-size:8.5px;color:#fff;line-height:11px;margin-bottom:12px;padding-left:10px}
.news li::before{content:"";position:absolute;left:0;top:2px;width:4px;height:4px;border-top:1.5px solid var(--gold);border-right:1.5px solid var(--gold);transform:rotate(45deg)}
.news li em{display:block;text-align:right;font-style:normal;font-weight:700;font-size:7px;color:var(--gold);margin-top:2px}

/* testimonials */
.testimonial{position:absolute;left:12px;top:886px;width:459px;height:104px;background:#f4f4f4;border:1px solid #d0d0d0}
.testimonial h3{position:absolute;left:13px;top:7px;font-weight:400;font-size:14.5px;color:#222}
.testimonial .quote{position:absolute;left:20px;top:32px;width:420px;text-align:center;font-family:"Didact Gothic",sans-serif;font-size:10.4px;line-height:13.5px;color:#333}
.testimonial .by{position:absolute;left:300px;top:78px;font-size:14px;color:var(--red)}

/* footer */
.site-footer{position:absolute;left:0;top:1008px;width:686px;height:162px;background:#fff;border-top:3px solid #2b2b2b}
.site-footer h4{position:absolute;font-weight:400;font-size:14.5px;color:#111}
.site-footer .rule{position:absolute;top:34px;left:0;width:686px;height:1px;background:#b9a97a}
.quick-links{position:absolute;left:13px;top:45px;list-style:none;font-family:Arial,sans-serif;font-size:9px;line-height:14px;color:#111}
.badges{position:absolute;left:196px;top:46px;width:190px}
.badges span{position:absolute;background:#d8d8d8;border:1px solid #888}
.contact{position:absolute;left:465px;top:0;width:220px;height:160px;font-family:Arial,sans-serif;font-size:8.5px;color:#111}
.contact .org{position:absolute;left:0;top:49px;color:var(--red);font-size:10px;white-space:nowrap}
.contact .row{position:absolute;left:0;display:flex;gap:8px;align-items:flex-start;line-height:11px}
.copyright{position:absolute;left:0;top:1172px;width:686px;height:28px;background:#2c2c2c;color:#ddd;font-size:7.5px;text-align:center;line-height:28px}
</style>
</head>
<body>

<header class="site-header">
  <div class="brand">
    <div class="brand-name">Thistlewaite<br>Auctioneers</div>
    <div class="brand-sub">INTERNATIONAL, LTD., INC</div>
  </div>
  <div class="brand-tag">"The Name That Closes!"</div>
  <div class="alliance">an alliance partner of Meridian Global</div>
  <div class="social" aria-label="Social links"><span></span><span></span><span></span><span></span></div>
  <svg class="phone-band" viewBox="0 0 208 28">
    <polygon points="20,3 208,3 198,14 208,25 20,25" fill="#c62f2d"/>
    <circle cx="16" cy="14" r="14" fill="#fff" stroke="#111" stroke-width="2"/>
    <path d="M10 8c1-1 2-1 3 0l2 3c.5 1 0 1.5-1 2 .8 2 2 3.2 4 4 .5-1 1-1.5 2-1l3 2c1 1 1 2 0 3-2 2-6 1-10-3s-5-8-3-10z" fill="#111"/>
  </svg>
  <div class="phone-band"><span class="txt">(555) 014 XXXX</span></div>
</header>

<nav class="main-nav">
  <a style="width:56px">Home</a>
  <a style="width:125px">Upcoming Auctions</a>
  <a style="width:112px">Online Auctions</a>
  <a style="width:78px">Real Estate</a>
  <a style="width:69px">Services</a>
  <a style="width:70px">About Us</a>
  <a style="width:70px">Gallery</a>
  <a style="width:106px;border-right:0">Contact Us</a>
</nav>

<div class="hero" role="img" aria-label="Slideshow photo of a white villa with a swimming pool and garden"></div>
<div class="hero-arrow" style="left:4px"></div>
<div class="hero-arrow" style="right:4px"></div>
<div class="hero-dots"><span class="on"></span><span></span><span></span><span></span></div>

<div class="dropdown">- Auctions 1<br>- Auctions 2<br>- Auctions 3</div>

<h1 class="welcome-title">Welcome to Thistlewaite Auctioneers International, Ltd, Inc</h1>
<p class="welcome-text">Lorem Ipsum. Proin gravida nibh vel velit auctor aliquet. Aenean sollicitudin, lorem quis bibendum auctor, nisi elit consequat ipsum, nec sagittis sem nibh id elit. Duis sed odio sit amet nibh vulputate cursus a sit amet mauris. Morbi accumsan ipsum velit. Nam nec tellus a odio tincidunt auctor a ornare odio. Sed non &nbsp;mauris vitae erat consequat auctor eu in elit.</p>

<aside class="newsletter">
  <div class="ico"></div>
  <h3>Sign up<br>Newsletter</h3>
  <div class="field">Enter Your Email Address..</div>
  <div class="btn">Subscribe</div>
</aside>

<h2 class="section-title" style="left:12px;top:548px">Current Auctions</h2>
<div class="pager">
  <span><svg width="8" height="10"><path d="M6 1L2 5l4 4" stroke="#fff" stroke-width="2" fill="none"/></svg></span>
  <span><svg width="8" height="10"><path d="M2 1l4 4-4 4" stroke="#fff" stroke-width="2" fill="none"/></svg></span>
</div>

<article class="auction-card" style="left:12px">
  <div class="head">LOREM IPSUM. PROIN GRAVIDA NIBH</div>
  <div class="photo" role="img" aria-label="Photo of a two-storey brick family house"></div>
  <div class="links"><span><i></i>Photo Galleries</span><span><i class="d"></i>Details</span></div>
  <div class="kind">LIVE ON-SITE AUCTION</div>
  <div class="meta" style="top:181px"><b>Begins:</b> Monday, 18-Nov-2013 at 4:00 PM</div>
  <div class="meta" style="top:199px"><b>Location:</b> Lorem Ipsum. Proin gravida nibh</div>
  <div class="bid"><i></i>Click Here to Bid Online Now!</div>
  <p>Lorem Ipsum. Proin gravida nibh vel velit auctor aliquet. Aenean sollicitudin, lorem quis bibendum auctor, nisi elit consequat ipsum, nec sagittis sem nibh id elit. Duis sed odio sit</p>
</article>

<article class="auction-card" style="left:245px">
  <div class="head">LOREM IPSUM. PROIN GRAVIDA NIBH</div>
  <div class="photo" role="img" aria-label="Photo of a two-storey brick family house"></div>
  <div class="links"><span><i></i>Photo Galleries</span><span><i class="d"></i>Details</span></div>
  <div class="kind">LIVE ON-SITE AUCTION</div>
  <div class="meta" style="top:181px"><b>Begins:</b> Monday, 18-Nov-2013 at 4:00 PM</div>
  <div class="meta" style="top:199px"><b>Location:</b> Lorem Ipsum. Proin gravida nibh</div>
  <div class="bid"><i></i>Click Here to Bid Online Now!</div>
  <p>Lorem Ipsum. Proin gravida nibh vel velit auctor aliquet. Aenean sollicitudin, lorem quis bibendum auctor, nisi elit consequat ipsum, nec sagittis sem nibh id elit. Duis sed odio sit</p>
</article>

<aside class="dark-widget upcoming" style="top:594px;height:191px">
  <div class="bar">Upcoming Auction</div>
  <div class="sub">Estate &amp; Consignment Auction</div>
  <div class="photo" role="img" aria-label="Photo of a country house with a lawn"></div>
  <div class="date">Start Date: Sunday 16-Nov-2013</div>
  <div class="btn">View more</div>
</aside>

<aside class="dark-widget news" style="top:811px;height:178px">
  <div class="bar">News &amp; Events</div>
  <ul>
    <li>Lorem Ipsum. Proin gravida mj nibh vel velit auctor aliquet op.<em>View details</em></li>
    <li>Lorem Ipsum. Proin gravida mj nibh vel velit auctor aliquet op.<em>View details</em></li>
    <li>Lorem Ipsum. Proin gravida mj nibh vel velit auctor aliquet op.<em>View details</em></li>
  </ul>
</aside>

<section class="testimonial">
  <h3>Clients Testimonials</h3>
  <p class="quote">Lorem Ipsum. Proin gravida nibh vel velit auctor aliquet. Aenean sollicitudin, lorem quis bibendum auctor, nisi elit consequat ipsum, nec sagittis sem nibh id elit. Duis sed odio sit amet nibh vulputate cursus a sit amet mauris.</p>
  <div class="by">- Daniel</div>
</section>

<footer class="site-footer">
  <h4 style="left:13px;top:8px">Quick link</h4>
  <h4 style="left:466px;top:8px">Contact Info</h4>
  <div class="rule"></div>
  <ul class="quick-links">
    <li>Home</li><li>Upcoming Auctions</li><li>Online Auctions</li><li>Real Estate</li>
    <li>Services</li><li>About Us</li><li>Auction Gallery</li><li>Contact Us</li>
  </ul>
  <div class="badges" aria-label="Partner badges">
    <span style="left:3px;top:0;width:22px;height:22px"></span>
    <span style="left:36px;top:4px;width:48px;height:18px"></span>
    <span style="left:98px;top:0;width:26px;height:22px"></span>
    <span style="left:136px;top:4px;width:48px;height:18px"></span>
    <span style="left:14px;top:40px;width:50px;height:16px"></span>
    <span style="left:78px;top:34px;width:30px;height:24px"></span>
    <span style="left:124px;top:34px;width:50px;height:24px"></span>
    <span style="left:44px;top:70px;width:56px;height:26px"></span>
    <span style="left:108px;top:74px;width:34px;height:20px"></span>
  </div>
  <div class="contact">
    <div class="org">Thistlewaite Auctioneers International, Inc</div>
    <div class="row" style="top:66px"><svg width="11" height="14"><path d="M5.5 1a4.5 4.5 0 0 0-4.5 4.5C1 9 5.5 13 5.5 13S10 9 10 5.5A4.5 4.5 0 0 0 5.5 1z" fill="#777"/><circle cx="5.5" cy="5.5" r="1.6" fill="#fff"/></svg><span>Lorem Ipsum. Proin gravida nibh vel<br>velit auctor aliquet. Aenean</span></div>
    <div class="row" style="top:100px"><svg width="11" height="14"><rect x="2" y="1" width="7" height="12" rx="1.5" fill="#777"/><rect x="3.2" y="3" width="4.6" height="7" fill="#fff"/></svg><span>(555) 014 XXXX</span></div>
    <div class="row" style="top:126px"><svg width="12" height="12"><rect x="3" y="1" width="6" height="3" fill="#777"/><rect x="1" y="4" width="10" height="5" fill="#777"/><rect x="3" y="8" width="6" height="3" fill="#aaa"/></svg><span>(555) 014 XXXX</span></div>
    <div class="row" style="top:148px"><svg width="12" height="10"><rect x="1" y="1" width="10" height="8" fill="#777"/><path d="M1 1l5 4 5-4" stroke="#fff" fill="none"/></svg><span>info@thistlewaite.com</span></div>
  </div>
</footer>

<div class="copyright">(c) 2013. Thistlewaite Auctioneers International, Ltd. Inc. All Rights Reserved.</div>

</body>
</html>
```